Create Vertical Dog Food Labels (3 inches x 5 inches) for PupKitchen

We need a packing Vertical label (3 inches x 5 inches) design for our line of Dog Food - Pup Kitchen at pupkitchenmeals.com (please review website). This design is for Custom Roll Labels. We have a logo already. Use our logo colors on label. What we need incorporated is a list of our ingredients:

50% Choice Beef
20% Pasture-raised Chicken
15% Brown Rice
15% Fresh Vegetables - Carrots, Kale, Zucchini
Herbal Health Boosters

We also need these lines at the bottom of the label:

Keeps in fridge for 4 days after thawing
Stores in freezer up to 6 months
Questions? email us at orders@meadowlanepantry.com

We have attached a sample of a competitor. The Kibble Crate.

Target Market(s)

Dog owners

Industry/Entity Type

Dog Food

Font styles to use
Sans Serif

Requirements
Must have
• Read project description above
Nice to have
• Our logo color incorporated
Should not have
• I want it simple.

```html
<!DOCTYPE html>
<html lang="en">
<head>
<meta charset="utf-8">
<title>PupKitchen – Nourishing Recipe Label</title>
<link rel="stylesheet" href="https://fonts.googleapis.com/css2?family=Roboto:wght@400;500&family=Roboto+Condensed:wght@500;700&family=Source+Sans+3:wght@700&family=Libre+Bodoni:wght@700&display=swap">
<style>
  :root {
    --page: #eeeeee;
    --label: #ffffff;
    --cream: #fcf1cf;
    --cream-line: #f6e2a8;
    --brand-green: #2e7d32;
    --brand-orange: #f39a1e;
    --red: #e31b23;
    --red-dark: #a8141a;
    --ink: #1a1a1a;
    --tan: #b89d63;
    --beige: #d9cbb5;
    --sky: #8fd3f3;
    --grey-panel: #f1f1f1;
  }
  * { box-sizing: border-box; margin: 0; padding: 0; }
  html, body { width: 1200px; height: 1200px; overflow: hidden; background: var(--page); }
  .label {
    position: absolute; left: 276px; top: 60px;
    width: 648px; height: 1080px;
    background: var(--label); border-radius: 22px; overflow: hidden;
    font-family: "Roboto", sans-serif; color: var(--ink);
    box-shadow: 0 4px 18px rgba(0,0,0,.12);
  }
  .brand-band {
    position: absolute; left: 0; top: 0; width: 100%; height: 206px;
    background: repeating-linear-gradient(180deg, var(--cream) 0 5px, var(--cream-line) 5px 7px);
  }
  .brand-dot {
    position: absolute; left: 101px; top: 49px; width: 128px; height: 128px;
    border-radius: 50%; background: var(--brand-green);
  }
  .brand-name {
    position: absolute; left: 274px; top: 104px;
    font-family: "Roboto", sans-serif; font-weight: 400; font-size: 50px;
    color: var(--brand-green); letter-spacing: 1px; line-height: 1;
  }
  .title {
    position: absolute; left: 0; top: 228px; width: 100%; text-align: center;
    font-family: "Source Sans 3", sans-serif; font-weight: 700; font-size: 72px;
    letter-spacing: -1.5px; line-height: 1; padding-left: 16px;
  }
  .dog-photo {
    position: absolute; left: 85px; top: 312px; width: 136px; height: 136px;
    border-radius: 50%; background: linear-gradient(180deg, var(--sky) 0 45%, #e2b27d 45%);
  }
  .ribbon { position: absolute; left: 214px; top: 313px; width: 400px; height: 122px; }
  .ribbon-text {
    position: absolute; left: 216px; top: 324px; width: 360px; text-align: center;
    font-family: "Source Sans 3", sans-serif; font-weight: 700; font-size: 60px;
    color: #fff; line-height: 1;
  }
  .deco { position: absolute; background: var(--beige); opacity: .85; }
  .deco-meat { left: 330px; top: 425px; width: 78px; height: 46px; border-radius: 40%; }
  .deco-cow { left: 0; top: 470px; width: 105px; height: 98px; border-radius: 14px; }
  .deco-carrot { left: 560px; top: 465px; width: 80px; height: 92px; border-radius: 40% 10% 40% 10%; }
  .deco-chicken { left: 0; top: 660px; width: 80px; height: 108px; border-radius: 45%; }
  .deco-kale { left: 556px; top: 640px; width: 92px; height: 112px; border-radius: 30%; }
  .ingredients {
    position: absolute; left: 121px; top: 494px; width: 422px; height: 280px;
    border: 2px solid var(--ink); border-radius: 36px; background: var(--grey-panel);
    display: grid; grid-template-columns: 1fr 1fr; grid-template-rows: 1fr 1fr;
    padding: 12px 14px 12px 10px; column-gap: 22px;
  }
  .ingredient {
    border-top: 2px solid var(--ink);
    display: flex; flex-direction: column; align-items: center;
    padding-top: 4px;
  }
  .ingredient:nth-child(-n+2) { margin: 0 12px; }
  .percent {
    font-family: "Libre Bodoni", serif; font-weight: 700; font-size: 56px; line-height: 1;
  }
  .percent small { font-size: 36px; }
  .pill {
    margin-top: 6px; background: var(--red); color: #fff; border-radius: 8px;
    font-family: "Roboto Condensed", sans-serif; font-weight: 700; font-size: 22px;
    padding: 3px 8px; text-align: center; line-height: 1.05; white-space: nowrap;
  }
  .pill small { display: block; font-size: 15px; font-weight: 500; }
  .storage {
    position: absolute; left: 2px; top: 822px; width: 446px; height: 80px;
    border-top: 2px solid var(--ink); border-bottom: 2px solid var(--ink);
    list-style: none; padding: 8px 0 0 16px;
    font-family: "Roboto Condensed", sans-serif; font-weight: 500; font-size: 23px; line-height: 31px;
  }
  .storage li::before { content: "–"; font-weight: 700; margin-right: 4px; }
  .boosters {
    position: absolute; left: 466px; top: 784px; width: 148px; height: 148px;
    border-radius: 50%; border: 3px solid var(--beige);
    display: flex; align-items: center; justify-content: center; text-align: center;
    font-family: "Roboto", sans-serif; font-size: 17px; line-height: 17px; color: #444;
    padding-top: 18px;
  }
  .contact-band {
    position: absolute; left: 0; top: 947px; width: 100%; height: 101px;
    background: var(--tan); color: #fff; text-align: center;
  }
  .contact-lead {
    font-family: "Roboto", sans-serif; font-weight: 500; font-size: 23px; letter-spacing: 2px;
    padding-top: 12px; padding-bottom: 10px;
    margin: 0 62px; border-bottom: 1.5px solid rgba(255,255,255,.8);
  }
  .contact-email { font-family: "Roboto", sans-serif; font-size: 31px; letter-spacing: 1px; padding-top: 6px; }
</style>
</head>
<body>
  <main class="label">
    <header class="brand-band">
      <span class="brand-dot"></span>
      <span class="brand-name">PupKitchen</span>
    </header>

    <h1 class="title">Nourishing Recipe</h1>

    <div class="dog-photo" role="img" aria-label="Photo of a happy dog"></div>
    <svg class="ribbon" viewBox="0 0 400 122" aria-hidden="true">
      <polygon points="320,60 400,70 380,96 400,122 320,112" fill="var(--red)"/>
      <polygon points="300,86 322,60 322,112" fill="var(--red-dark)"/>
      <path d="M0,10 Q150,-8 320,20 L320,88 Q150,64 6,96 Z" fill="var(--red)"/>
    </svg>
    <div class="ribbon-text">For Dogs</div>

    <div class="deco deco-meat" role="img" aria-label="Steak icon"></div>
    <div class="deco deco-cow" role="img" aria-label="Cow illustration"></div>
    <div class="deco deco-carrot" role="img" aria-label="Carrot illustration"></div>
    <div class="deco deco-chicken" role="img" aria-label="Chicken illustration"></div>
    <div class="deco deco-kale" role="img" aria-label="Kale leaf illustration"></div>

    <section class="ingredients">
      <div class="ingredient">
        <span class="percent">50<small>%</small></span>
        <span class="pill">Choice Beef</span>
      </div>
      <div class="ingredient">
        <span class="percent">15<small>%</small></span>
        <span class="pill">Brown Rice</span>
      </div>
      <div class="ingredient">
        <span class="percent">20<small>%</small></span>
        <span class="pill">Pasture-raised<br>Chicken</span>
      </div>
      <div class="ingredient">
        <span class="percent">15<small>%</small></span>
        <span class="pill">Fresh Vegetables<small>(Carrots, Kale, Zucchini)</small></span>
      </div>
    </section>

    <ul class="storage">
      <li>Keeps in fridge for 4 days after thawing</li>
      <li>Stores in freezer up to 6 months</li>
    </ul>

    <div class="boosters">HERBAL<br>HEALTH<br>BOOSTERS</div>

    <footer class="contact-band">
      <p class="contact-lead">QUESTIONS? EMAIL US AT</p>
      <p class="contact-email">orders@meadowlanepantry.com</p>
    </footer>
  </main>
</body>
</html>
```